Bref créative
Business Cards and Stationary for KRVMD
Modern
Warren Fitzhugh
Managing Partner
4185 Marlow Avenue, Suite 312
San Antonio TX 78249-6172
210-555-0148 x3092
warren@kr-vmd.example
www.kr-vmd.example
Logo Details
Font: Myriad Pro
Colors
BLUE C=85 M=50 Y=0 K=0
RED C=0 M=100 Y=100 K=0
GREY C=0 M=0 Y=0 K=90
Ai Logo Files

```html
<!DOCTYPE html>
<html lang="en">
<head>
<meta charset="utf-8">
<title>KRVMD Business Cards</title>
<link href="https://fonts.googleapis.com/css2?family=Source+Sans+3:wght@400;600;700&display=swap" rel="stylesheet">
<style>
  :root {
    --blue: #2a7fd4;
    --blue-dark: #1f63ad;
    --red: #e2231a;
    --grey: #3a3a3a;
    --grey-soft: #7a7a7a;
    --card: #ffffff;
    --backdrop: #e9eaec;
  }
  * { box-sizing: border-box; margin: 0; padding: 0; }
  html, body {
    width: 1200px; height: 864px; overflow: hidden;
    background: var(--backdrop);
    font-family: "Source Sans 3", "Myriad Pro", sans-serif;
    color: var(--grey);
  }
  .sheet {
    width: 1200px; height: 864px;
    display: flex; align-items: center; justify-content: center; gap: 40px;
  }
  .card {
    position: relative;
    width: 540px; height: 309px;
    background: var(--card);
    border-radius: 14px;
    overflow: hidden;
    box-shadow: 0 10px 28px rgba(0,0,0,.18);
  }
  .brand {
    display: flex; align-items: center; gap: 12px;
  }
  .brand-dot {
    width: 18px; height: 18px; border-radius: 50%;
    background: var(--red);
  }
  .brand-name {
    font-weight: 700; color: var(--blue);
    letter-spacing: 1px;
  }

  /* front */
  .card-front .brand {
    position: absolute; left: 0; right: 0; top: 110px;
    justify-content: center;
  }
  .card-front .brand-name { font-size: 56px; }
  .card-front .web {
    position: absolute; left: 0; right: 0; top: 192px;
    text-align: center;
    font-size: 13px; letter-spacing: 4px; color: var(--grey-soft);
  }

  /* back */
  .card-back .swoosh { position: absolute; left: 0; bottom: 0; }
  .card-back .brand {
    position: absolute; left: 36px; top: 110px;
  }
  .card-back .brand-dot { width: 14px; height: 14px; }
  .card-back .brand-name { font-size: 40px; }
  .person {
    position: absolute; left: 40px; top: 178px;
    line-height: 1.2;
  }
  .person-name { font-size: 13px; font-weight: 700; color: var(--blue-dark); }
  .person-title { font-size: 11px; color: var(--grey-soft); }
  .contact {
    position: absolute; left: 320px; top: 48px;
    list-style: none;
    font-size: 11.5px; color: var(--grey);
  }
  .contact li {
    display: flex; align-items: center; gap: 8px;
    height: 19px;
  }
  .contact .icon {
    width: 13px; height: 13px; flex: none;
  }
  .contact .plain { padding-left: 21px; }
</style>
</head>
<body>
<main class="sheet">

  <section class="card card-front" aria-label="Card front">
    <div class="brand">
      <span class="brand-dot"></span>
      <span class="brand-name">KRVMD</span>
    </div>
    <p class="web">www.kr-vmd.example</p>
  </section>

  <section class="card card-back" aria-label="Card back">
    <svg class="swoosh" width="540" height="309" viewBox="0 0 540 309" aria-hidden="true">
      <path d="M0 190 C 60 250, 180 270, 300 262 C 400 255, 470 240, 540 228 L540 309 L0 309 Z" fill="var(--blue)"/>
      <path d="M120 309 C 220 272, 360 262, 540 250 L540 309 Z" fill="var(--red)"/>
      <path d="M0 190 C 50 232, 140 256, 240 262 C 150 262, 60 245, 0 218 Z" fill="var(--blue-dark)"/>
    </svg>

    <div class="brand">
      <span class="brand-dot"></span>
      <span class="brand-name">KRVMD</span>
    </div>
    <div class="person">
      <p class="person-name">Warren Fitzhugh</p>
      <p class="person-title">Managing Partner</p>
    </div>

    <ul class="contact">
      <li>
        <svg class="icon" viewBox="0 0 14 14" aria-hidden="true"><circle cx="7" cy="7" r="7" fill="var(--blue)"/><path d="M7 3.2a2.3 2.3 0 0 1 2.3 2.3C9.3 7.3 7 10.6 7 10.6S4.7 7.3 4.7 5.5A2.3 2.3 0 0 1 7 3.2z" fill="#fff"/></svg>
        KRVMD LLC
      </li>
      <li class="plain">4185 Marlow Avenue, Suite 312</li>
      <li class="plain">San Antonio TX 78249-6172</li>
      <li>
        <svg class="icon" viewBox="0 0 14 14" aria-hidden="true"><circle cx="7" cy="7" r="7" fill="var(--blue)"/><path d="M4.6 3.6l1.4-.3.8 1.8-.9.7c.4.9 1.1 1.6 2 2l.7-.9 1.8.8-.3 1.4c-3 .2-5.7-2.5-5.5-5.5z" fill="#fff"/></svg>
        210-555-0148 x3092
      </li>
      <li>
        <svg class="icon" viewBox="0 0 14 14" aria-hidden="true"><circle cx="7" cy="7" r="7" fill="var(--blue)"/><rect x="3.6" y="4.6" width="6.8" height="4.8" fill="#fff"/><path d="M3.6 4.6L7 7.3l3.4-2.7" fill="none" stroke="var(--blue)" stroke-width=".8"/></svg>
        warren@kr-vmd.example
      </li>
      <li>
        <svg class="icon" viewBox="0 0 14 14" aria-hidden="true"><circle cx="7" cy="7" r="7" fill="var(--blue)"/><circle cx="7" cy="7" r="3.4" fill="none" stroke="#fff" stroke-width=".9"/><path d="M3.6 7h6.8M7 3.6c-1.4 1.8-1.4 5 0 6.8M7 3.6c1.4 1.8 1.4 5 0 6.8" fill="none" stroke="#fff" stroke-width=".7"/></svg>
        www.kr-vmd.example
      </li>
    </ul>
  </section>

</main>
</body>
</html>
```